Corvel Tide Supply Business Cards

I need a business card design for my business. We specialise in supplying quality brand cleaning products for boats
Updates

Target Market(s)

local household people with personal boats

Industry/Entity Type

Business

Requirements
Must have
• Address - 14 Fenwick Turn, Marlow WA 6802
Phone - 0461 382 917
Email - corveltidesupply@quillnet.com
Web - www.corveltidesupply.com.au
Warren Hale
Director

Business logo is a must have
Nice to have
• Glennox logo is optional but recommended as it shows what we do

```html
<!DOCTYPE html>
<html lang="en">
<head>
<meta charset="utf-8">
<title>Corvel Tide Supply Business Cards</title>
<link rel="stylesheet" href="https://fonts.googleapis.com/css2?family=Source+Sans+3:wght@400;600;700&display=swap">
<style>
  :root {
    --brand-blue: #0b5690;
    --brand-blue-text: #1a5c96;
    --divider-blue: #8fb0cf;
    --card-white: #ffffff;
    --stage-grey: #d4d4d4;
  }
  * { box-sizing: border-box; margin: 0; padding: 0; }
  html, body { width: 1200px; height: 900px; overflow: hidden; }
  body {
    background: var(--stage-grey);
    font-family: "Source Sans 3", "Myriad Pro", Arial, sans-serif;
    display: flex;
    align-items: center;
    justify-content: center;
    gap: 48px;
  }
  .card {
    width: 520px;
    height: 297px;
    position: relative;
    box-shadow: 0 6px 18px rgba(0,0,0,0.18);
  }
  .card--front {
    background: var(--brand-blue);
    display: flex;
    align-items: center;
    justify-content: center;
  }
  .brand {
    display: flex;
    align-items: center;
    gap: 12px;
    font-weight: 600;
    letter-spacing: 0.06em;
    text-transform: uppercase;
  }
  .brand__dot {
    width: 14px;
    height: 14px;
    border-radius: 50%;
    flex-shrink: 0;
  }
  .card--front .brand { color: var(--card-white); font-size: 26px; }
  .card--front .brand__dot { background: var(--card-white); }

  .card--back {
    background: var(--card-white);
    display: flex;
  }
  .card__logo-side {
    width: 47%;
    display: flex;
    align-items: center;
    justify-content: center;
  }
  .card--back .brand { color: var(--brand-blue-text); font-size: 17px; }
  .card--back .brand__dot { background: var(--brand-blue-text); width: 11px; height: 11px; }
  .card__divider {
    width: 1px;
    background: var(--divider-blue);
    margin: 30px 0;
  }
  .card__details {
    flex: 1;
    padding: 30px 30px 34px 20px;
    display: flex;
    flex-direction: column;
    justify-content: space-between;
    text-align: right;
    color: var(--brand-blue-text);
  }
  .person__name { font-weight: 700; font-size: 17px; line-height: 1.1; }
  .person__role { font-size: 12px; line-height: 1.3; }
  .contact { font-style: normal; font-size: 13.5px; line-height: 1.35; }
  .contact__gap { margin-top: 10px; }
</style>
</head>
<body>
  <section class="card card--front" aria-label="Card front">
    <div class="brand"><span class="brand__dot"></span>Corvel Tide Supply</div>
  </section>

  <section class="card card--back" aria-label="Card back">
    <div class="card__logo-side">
      <div class="brand"><span class="brand__dot"></span>Corvel Tide Supply</div>
    </div>
    <div class="card__divider"></div>
    <div class="card__details">
      <div class="person">
        <p class="person__name">Warren Hale</p>
        <p class="person__role">Director</p>
      </div>
      <address class="contact">
        <p>14 Fenwick Turn, Marlow WA 6802</p>
        <p>0461 382 917</p>
        <p class="contact__gap">corveltidesupply@quillnet.com</p>
        <p>www.corveltidesupply.com.au</p>
      </address>
    </div>
  </section>
</body>
</html>
```